Improved Business Card, Government Contracting

We are looking to update the design of our business cards. We would like to create a template that can be used for future employees and easy to update.

Halvorsen Advisory Partners, LLC is a Service Disabled Veteran Owned Small Business with headquarters located in Leavenworth, KS. Our current website is www.hapteam.com. We have contracts in KS and VA with expansion opportunities in various other states. Our primary line of work is within government contracting and providing consulting services to various organizations within the Bureau of Frontier Works. We would like to project a professional image of our company that is consistent with the industry. Provided are previous versions of our business card template that shows our logo as well. We would like to make sure the information on the cards are easily noticeable .

Target Market(s)

Government Officials
Fellow Small Business Contractors
Large Business Contractors (ex. TRUX, Keswell Barnaby, Pryde Okonjo Whitcombe)

Industry/Entity Type

Business

Contact Information for Business Card

Dale Fenwick
Office Manager
Halvorsen Advisory Partners
Ph: 913.555.0172
Email: d.fenwick@hapteam.us
www.hapteam.com

Requirements
Must have
• The business mailing address is:
• 31842 204th Lane
• Leavenworth, KS 66099
Nice to have
• Embossed lettering

```html
<!DOCTYPE html>
<html lang="en">
<head>
<meta charset="utf-8">
<title>Halvorsen Advisory Partners – Business Card</title>
<link rel="stylesheet" href="https://fonts.googleapis.com/css2?family=Montserrat:wght@600&family=Quicksand:wght@400;500&display=swap">
<style>
  :root {
    --page-bg: #e6e6e4;
    --brand-blue: #3f5fb4;
    --brand-blue-deep: #334f9f;
    --brand-blue-light: #6a84c8;
    --card-white: #f1f1f1;
    --accent-yellow: #f0e860;
    --text-light: #eef1fa;
  }
  html, body {
    margin: 0;
    padding: 0;
    width: 1200px;
    height: 1000px;
    overflow: hidden;
    background: var(--page-bg);
  }
  .canvas {
    position: relative;
    width: 1200px;
    height: 1000px;
  }
  .card {
    position: absolute;
    left: 220px;
    width: 760px;
    height: 434px;
    box-shadow: 0 6px 18px rgba(0,0,0,0.18);
  }
  .card--front { top: 46px; }
  .card--back  { top: 520px; }
  .card svg { display: block; }

  .brand-name {
    font-family: "Quicksand", sans-serif;
    font-weight: 500;
    fill: var(--brand-blue);
  }
  .person-name {
    font-family: "Montserrat", sans-serif;
    font-weight: 600;
    font-size: 27px;
    fill: #ffffff;
  }
  .contact-line {
    font-family: "Quicksand", sans-serif;
    font-weight: 400;
    font-size: 17px;
    fill: var(--text-light);
  }
  .icon { fill: var(--accent-yellow); }
  .name-rule { fill: var(--accent-yellow); }
</style>
</head>
<body>
<main class="canvas">

  <!-- Front of card -->
  <section class="card card--front" aria-label="Business card front">
    <svg width="760" height="434" viewBox="0 0 760 434">
      <defs>
        <linearGradient id="frontBlue" x1="0" y1="1" x2="1" y2="0">
          <stop offset="0" stop-color="var(--brand-blue-deep)"/>
          <stop offset="0.6" stop-color="var(--brand-blue)"/>
          <stop offset="1" stop-color="var(--brand-blue-light)"/>
        </linearGradient>
      </defs>
      <rect class="card-field" width="760" height="434" fill="url(#frontBlue)"/>
      <polygon class="white-band" points="120,434 320,0 640,0 440,434" fill="var(--card-white)"/>
      <text class="brand-name" x="380" y="208" font-size="25" text-anchor="middle">Halvorsen</text>
      <text class="brand-name" x="380" y="240" font-size="25" text-anchor="middle">Advisory Partners</text>
    </svg>
  </section>

  <!-- Back of card -->
  <section class="card card--back" aria-label="Business card back">
    <svg width="760" height="434" viewBox="0 0 760 434">
      <defs>
        <linearGradient id="backBlue" x1="0" y1="1" x2="1" y2="0">
          <stop offset="0" stop-color="var(--brand-blue-deep)"/>
          <stop offset="0.55" stop-color="var(--brand-blue-light)"/>
          <stop offset="1" stop-color="var(--brand-blue)"/>
        </linearGradient>
      </defs>
      <rect class="card-field" width="760" height="434" fill="url(#backBlue)"/>
      <polygon class="white-wedge" points="0,0 340,217 0,434" fill="var(--card-white)"/>
      <text class="brand-name" x="135" y="212" font-size="20" text-anchor="middle">Halvorsen</text>
      <text class="brand-name" x="135" y="238" font-size="20" text-anchor="middle">Advisory Partners</text>

      <!-- Name block -->
      <rect class="name-rule" x="404" y="52" width="4" height="84"/>
      <text class="person-name" x="422" y="80">Dale Fenwick</text>
      <text class="contact-line" x="422" y="106">Halvorsen Advisory Partners</text>
      <text class="contact-line" x="422" y="128">LLC Office Manager</text>

      <!-- Address -->
      <path class="icon" d="M430 160a7 7 0 0 1 7 7c0 5-7 12-7 12s-7-7-7-12a7 7 0 0 1 7-7zm0 4a3 3 0 1 0 0 6a3 3 0 0 0 0-6z"/>
      <text class="contact-line" x="450" y="174">4410 Harlan Row</text>
      <text class="contact-line" x="450" y="196">Suite C</text>
      <text class="contact-line" x="450" y="218">Leavenworth, KS 66099</text>

      <!-- Phones -->
      <path class="icon" d="M424 244c2-2 4-2 5 0l2 3c1 1 0 3-1 3c1 3 3 5 6 6c0-1 2-2 3-1l3 2c2 1 2 3 0 5c-8 2-20-10-18-18z"/>
      <text class="contact-line" x="450" y="258">913.555.0148</text>
      <rect class="icon" x="423" y="272" width="14" height="12" rx="2"/>
      <text class="contact-line" x="450" y="284">913.555.0163</text>

      <!-- Web & mail -->
      <circle class="icon" cx="430" cy="304" r="7"/>
      <text class="contact-line" x="450" y="310">www.hapteam.com</text>
      <rect class="icon" x="423" y="325" width="14" height="10" rx="1"/>
      <text class="contact-line" x="450" y="336">d.fenwick@hapteam.us</text>
    </svg>
  </section>

</main>
</body>
</html>
```